A new PowerPoint Template for a French consulting company

Who are we?

Formed in 2005, Quorv is a consulting company specialising in the human aspect of change and transformation.

From our offices in the heart of Paris, our team of 30 consultants work with leading organisations in the Aerospace, Finance, Transportation and Public sectors to deliver lasting change.

Our customers trust us with some of their most strategic and sensitive projects. They trust us with these projects because:
- We listen to them, ensuring we understand the real needs of their business
- We involve them, co-developing and tailoring our solutions to the specific challenges they face
- We’re professional, without taking ourselves too seriously
- We’re imaginative, whilst always remaining pragmatic
- We get results!

You can find out more about who we are and the work we do here: http://www.quorv-example.fr/en

What we need from you?

We’re approaching our 10th birthday and, whilst we still love what we do, we think it’s the right time to update our image.

We’d like you to design us a new PowerPoint template, that will be used for all of our internal and client facing work. You can base your submissions on our existing logo and colour scheme (see files attached) or you can submit your own fresh ideas – after all, we’re not afraid of change!

Finally, whilst we’re looking for you to be creative, there are some simple guidelines that we need you to keep in mind:

1. The Template needs to include both a front cover and a “content” page

2. The front cover needs to:
- Include our logo
- Reflect “who we are” and the type of work that we do

3. The content page needs to:
- Have a predominantly white background
- Be practical to use, making an effective use of the 4:3 standard PPT size
- Include an area across the top of the page for the slide title
- Include areas along the bottom of the page for the page number and date

4. If you decide to propose a new colour scheme, it should be balanced and the “accents” usable

5. The PowerPoint Template needs to be “printer friendly”

6. The fonts you use should be standard

What we don’t want?

To give you as much help as possible, here are some things that we really don’t want:

- Submissions that are dull grey or navy blue, suggesting we’re nothing but boring corporate suits
- Submissions that are Lulette pink or too “soft and cuddly”
- Submissions that use lots of stock images of “happy, smiling, consultants”
- Submissions that will be the height of fashion today, but completely out of date next year

```html
<!DOCTYPE html>
<html lang="en">
<head>
<meta charset="utf-8">
<title>Quorv – Our Service</title>
<link rel="stylesheet" href="https://fonts.googleapis.com/css2?family=Carlito:ital,wght@0,400;0,700;1,400&display=swap">
<style>
  :root {
    --maroon: #6a0d3b;
    --teal: #2fb3a7;
    --teal-deep: #259a8f;
    --teal-light: #4fc2b7;
    --ink: #444444;
    --body-ink: #4a4a4a;
    --white: #ffffff;
  }
  * { margin: 0; padding: 0; box-sizing: border-box; }
  html, body { width: 1200px; height: 900px; overflow: hidden; background: var(--white); }
  body { font-family: "Carlito", "Calibri", Arial, sans-serif; }
  .slide { position: relative; width: 1200px; height: 900px; overflow: hidden; background: var(--white); }

  .top-rule { position: absolute; left: 0; top: 0; width: 602px; height: 9px; background: var(--maroon); }

  .brand { position: absolute; left: 63px; top: 30px; }
  .brand-name { font-size: 58px; font-weight: 700; color: var(--maroon); line-height: 1; }

  .intro { position: absolute; left: 63px; top: 158px; width: 475px; }
  .slide-title { font-size: 45px; font-weight: 700; color: var(--ink); letter-spacing: 0.5px; line-height: 1; }
  .intro-text { margin-top: 55px; font-size: 24px; line-height: 32.7px; color: var(--body-ink); hyphens: auto; }
  .intro-caption { margin-top: 30px; font-size: 16px; font-style: italic; line-height: 22px; color: var(--body-ink); text-align: center; padding: 0 40px; }

  .visual-panel {
    position: absolute; left: 602px; top: 0; width: 598px; height: 900px;
    background:
      linear-gradient(180deg, rgba(47,179,167,0.0) 0%, rgba(37,154,143,0.35) 100%),
      radial-gradient(ellipse at 60% 55%, var(--teal-light) 0%, var(--teal) 55%, var(--teal-deep) 100%);
  }

  .service-list { position: absolute; left: 642px; top: 156px; width: 520px; list-style: none; }
  .service-item { position: relative; height: 191px; padding-left: 93px; color: var(--white); }
  .service-number { position: absolute; left: 0; top: 0; font-size: 20px; font-weight: 700; }
  .service-icon { position: absolute; left: 50px; top: -2px; width: 28px; height: 30px; }
  .service-heading { font-size: 19px; font-weight: 700; line-height: 26px; }
  .service-text { margin-top: 14px; font-size: 14.5px; line-height: 20px; width: 372px; }

  .page-number { position: absolute; left: 1115px; top: 845px; width: 34px; height: 32px; }
  .page-number span { position: absolute; left: 0; top: 0; width: 28px; line-height: 32px; text-align: center; color: var(--white); font-size: 16px; }
</style>
</head>
<body>
<div class="slide">
  <div class="top-rule"></div>

  <div class="brand">
    <div class="brand-name">Quorv</div>
  </div>

  <section class="intro">
    <h1 class="slide-title">OUR SERVICE</h1>
    <p class="intro-text">Sed ut perspiciatis unde omnis iste natus error sit voluptatem accusantium doloremque lau&shy;dantium, totam rem aperiam, eaque ipsa quae ab illo inventore veritatis et quasi archi&shy;tecto beatae vitae dicta sunt explicabo. Nemo enim ipsam voluptatem quia voluptas sit aspernatur aut odit aut fugit, sed quia conse&shy;quuntur magni dolores eos qui ratione voluptatem sequi nesciunt. Neque porro quisquam est, qui dolorem ipsum quia dolor sit amet, consectetur, adipisci velit, sed quia non numquam</p>
    <p class="intro-caption">eius modi tempora incidunt ut labore et dolore magnam aliquam</p>
  </section>

  <div class="visual-panel" role="img" aria-label="Photograph of a modern glass office building, tinted in teal"></div>

  <ol class="service-list">
    <li class="service-item">
      <span class="service-number">1.</span>
      <svg class="service-icon" viewBox="0 0 28 30" fill="none" stroke="#fff" stroke-width="2.4">
        <rect x="5" y="2" width="18" height="26" rx="2"/>
        <line x1="9" y1="9" x2="19" y2="9"/><line x1="9" y1="14" x2="19" y2="14"/><line x1="9" y1="19" x2="19" y2="19"/><line x1="9" y1="24" x2="15" y2="24"/>
      </svg>
      <h2 class="service-heading">At vero eos et accusamus</h2>
      <p class="service-text">sed quia non numquam eius modi tempora incidunt ut labore et dolore magnam aliquam quaerat voluptatem. Ut enim ad minima veniam, quis nostrum exercitationem ullam corporis suscipit laboriosam</p>
    </li>
    <li class="service-item">
      <span class="service-number">2.</span>
      <svg class="service-icon" viewBox="0 0 28 30" fill="none" stroke="#fff" stroke-width="2.4">
        <rect x="2" y="5" width="24" height="22" rx="2"/>
        <rect x="2" y="5" width="24" height="6" fill="#fff"/>
        <line x1="8" y1="1" x2="8" y2="7"/><line x1="20" y1="1" x2="20" y2="7"/>
      </svg>
      <h2 class="service-heading">At vero eos et accusamus</h2>
      <p class="service-text">sed quia non numquam eius modi tempora incidunt ut labore et dolore magnam aliquam quaerat voluptatem. Ut enim ad minima veniam, quis nostrum exercitationem ullam corporis suscipit laboriosam</p>
    </li>
    <li class="service-item">
      <span class="service-number">3.</span>
      <svg class="service-icon" viewBox="0 0 28 30" fill="none" stroke="#fff" stroke-width="2.4">
        <rect x="6" y="1" width="16" height="28" rx="3"/>
        <line x1="6" y1="23" x2="22" y2="23"/>
        <circle cx="14" cy="26" r="0.8" fill="#fff"/>
      </svg>
      <h2 class="service-heading">At vero eos et accusamus</h2>
      <p class="service-text">sed quia non numquam eius modi tempora incidunt ut labore et dolore magnam aliquam quaerat voluptatem. Ut enim ad minima veniam, quis nostrum exercitationem ullam corporis suscipit laboriosam</p>
    </li>
  </ol>

  <div class="page-number">
    <svg width="34" height="32" viewBox="0 0 34 32"><polygon points="0,0 26,0 34,16 26,32 0,32" fill="var(--maroon)"/></svg>
    <span>2</span>
  </div>
</div>
</body>
</html>
```